Name card for fertilizer industry

We 1. produce liquid fertilizer 2. gardening supply 3. Import&Export gardening related product.
I want the name card double-sided(Chinese & English version)
detail has chinese charactor for name and address.
Updates
Target Market(s)
Farmers
Industry/Entity Type
Industry
Contact Information for Business Card
Name: Martin Lo (邱偉達)
TEL: +886-47-615204
FAX:+886-47-640173
MOBILE: +886-952-184-603
ADDRESS: No.58, Taoyuan Rd, Beiming Township, Lanping County , TAIWAN(R.O.C) 蘭平縣北明鎮桃源路58號
Look and feel
Each slider illustrates characteristics of the customer's brand and the style your logo design should communicate.

```html
<!DOCTYPE html>
<html lang="en">
<head>
<meta charset="utf-8">
<title>Verdance Enterprise Co. – Name Card</title>
<link rel="stylesheet" href="https://fonts.googleapis.com/css2?family=Raleway:wght@400;500&family=Noto+Sans+TC:wght@400;500&display=swap">
<style>
  :root {
    --backdrop: #ebe6df;
    --card: #ffffff;
    --brand-green: #72ab34;
    --brand-green-light: #8fc640;
    --brand-brown: #5b4d47;
    --body-grey: #7a7471;
  }
  * { margin: 0; padding: 0; box-sizing: border-box; }
  html, body {
    width: 1200px; height: 749px; overflow: hidden;
    background: var(--backdrop);
  }
  .stage { position: relative; width: 1200px; height: 749px; }

  .card {
    position: absolute; top: 200px; height: 310px;
    background: var(--card);
    box-shadow: 0 18px 30px rgba(60, 45, 30, 0.18);
    overflow: hidden;
  }
  .card--front { left: 39px; width: 547px; }
  .card--back  { left: 621px; width: 544px; }

  .brand-circle {
    position: absolute; border: 2px solid var(--brand-green); border-radius: 50%;
  }
  .card--front .brand-circle { left: 218px; top: 72px; width: 112px; height: 112px; }
  .card--back  .brand-circle { left: 231px; top: 29px; width: 68px; height: 68px; }

  .brand-name {
    position: absolute; left: 0; right: 0; text-align: center;
    font-family: "Raleway", sans-serif; font-weight: 400;
    color: var(--brand-brown); letter-spacing: 0.2px; white-space: nowrap;
  }
  .card--front .brand-name { top: 185px; font-size: 26px; }
  .card--back  .brand-name { top: 107px; font-size: 18px; left: 10px; }

  .contact-en { position: absolute; left: 27px; top: 151px; font-family: "Raleway", sans-serif; }
  .contact-zh { position: absolute; right: 27px; top: 151px; text-align: right; font-family: "Noto Sans TC", sans-serif; }

  .person-name { color: var(--brand-green); font-size: 17px; font-weight: 500; line-height: 22px; }
  .contact-en .person-name { font-family: "Raleway", sans-serif; }

  .address { color: var(--body-grey); font-size: 12.5px; line-height: 16px; margin-top: 5px; }
  .contact-zh .address { font-size: 13px; margin-top: 2px; }

  .phone-list { list-style: none; margin-top: 4px; }
  .phone-list li {
    display: flex; align-items: center; gap: 5px;
    color: var(--body-grey); font-size: 12.5px; line-height: 15px;
  }
  .phone-list svg { width: 10px; height: 10px; fill: var(--brand-green); flex: none; }

  .accent-band {
    position: absolute; left: 0; right: 0; bottom: 0; height: 24px;
    background: linear-gradient(90deg, var(--brand-green-light), var(--brand-green));
  }
</style>
</head>
<body>
<main class="stage">
  <section class="card card--front" aria-label="Card front">
    <div class="brand-circle"></div>
    <p class="brand-name">VERDANCE ENTERPRISE CO.</p>
  </section>

  <section class="card card--back" aria-label="Card back">
    <div class="brand-circle"></div>
    <p class="brand-name">VERDANCE ENTERPRISE CO.</p>

    <div class="contact-en">
      <p class="person-name">Martin Lo</p>
      <p class="address">No.58, Taoyuan Rd, Beiming<br>Township, Lanping<br>County , TAIWAN(R.O.C)</p>
      <ul class="phone-list">
        <li><svg viewBox="0 0 10 10" aria-label="Mobile"><path d="M2.5 0h5a1 1 0 0 1 1 1v8a1 1 0 0 1-1 1h-5a1 1 0 0 1-1-1V1a1 1 0 0 1 1-1zm.5 1.5v6h4v-6z"/></svg>+886-47-615204</li>
        <li><svg viewBox="0 0 10 10" aria-label="Telephone"><path d="M0 3.5C1 1 9 1 10 3.5L9 5 7 4.2V3.2C5.7 2.8 4.3 2.8 3 3.2v1L1 5zM2 6h6l1 3H1z"/></svg>+886-47-640173</li>
        <li><svg viewBox="0 0 10 10" aria-label="Fax"><path d="M2.5 0h5v3h-5zM0 3.5h10V8H8.5v2h-7V8H0zm2.5 3v2.5h5V6.5z"/></svg>+886-952-184-603</li>
      </ul>
    </div>

    <div class="contact-zh" lang="zh-Hant">
      <p class="person-name">邱偉達</p>
      <p class="address">蘭平縣北明鎮桃源路58號</p>
    </div>

    <div class="accent-band"></div>
  </section>
</main>
</body>
</html>
```